Custom Vinyl Wrap Design

I need a custom vinyl wrap design for a saw. This wrap is going to cover a saw that is used to cut stone. Please view the attached Jped document for my ideas and more design details.
Thank you.
Updates
The top and side of the saw should be one graphic because they are both one piece. The two ends of the saw should be two separate graphics. The "TusklineDrill Cutter" logo should be on the side of the saw. Please insure the Emergency Shut Off graphic is ergonomic and is more rectangular in shape as apposed to being a square label that takes up allot of room...
Hey guys, I am on a tight deadline for this project. It would be great to see some designs by the middle of the week if possible.
I would like to see some more graphics soon if possible. Dont worry about not getting all the dimensions exact for now. I just want to see everyone's individual style and interpretation of what I am looking for. Once I see everyone's style, I will chose the one designer to work closer with.
Target Market(s)
industrial, mining, construction
Requirements
Must have
- Branded logo
Made in Canada Logo
Eco friendly logo
Emergency Shut off label incorporated into the design
on-off-reset labels also incorporated into the design

```html
<!DOCTYPE html>
<html lang="en">
<head>
<meta charset="utf-8">
<title>TusklineDrill Cutter — Vinyl Wrap Designs</title>
<link rel="stylesheet" href="https://fonts.googleapis.com/css2?family=Oswald:wght@400;600;700&family=Roboto:wght@300&display=swap">
<style>
  :root {
    --ink: #1a1a1a;
    --asphalt-dark: #141619;
    --asphalt-mid: #2b3038;
    --slate-blue: #3a4a5e;
    --accent-blue: #29abe2;
    --hazard-yellow: #f7e51a;
    --hazard-black: #111111;
    --alert-red: #ec1c24;
    --chalk: #ffffff;
    --muted-grey: #a7a9ac;
    --faint-grey: #8d9197;
  }
  * { box-sizing: border-box; margin: 0; padding: 0; }
  html, body { width: 1200px; height: 1000px; overflow: hidden; background: var(--chalk); }
  .sheet { position: relative; width: 1200px; height: 1000px; font-family: "Oswald", sans-serif; }

  .panel { position: absolute; overflow: hidden; }
  .texture {
    position: absolute; inset: 0;
    background:
      linear-gradient(115deg, transparent 30%, rgba(58,74,94,.55) 45%, transparent 65%),
      radial-gradient(ellipse at 30% 40%, var(--asphalt-mid), var(--asphalt-dark) 75%);
  }
  .panel svg.overlay { position: absolute; inset: 0; width: 100%; height: 100%; }

  /* Title block */
  .title-block { position: absolute; right: 30px; top: 40px; text-align: right; }
  .brand-name {
    font-family: "Oswald", sans-serif; font-weight: 700; color: var(--ink);
    line-height: .95; letter-spacing: 1px;
  }
  .brand-name .line-1 { display: block; font-size: 104px; }
  .brand-name .line-2 { display: block; font-size: 74px; margin-right: 20px; }
  .title-caption {
    font-family: "Roboto", sans-serif; font-weight: 300; font-size: 34px;
    color: var(--muted-grey); margin-top: 14px; margin-right: 40px; word-spacing: 10px;
  }

  /* End panel A */
  .end-panel { left: 35px; top: 25px; width: 400px; height: 200px; }

  /* Top & side panel */
  .side-panel { left: 35px; top: 232px; width: 400px; height: 513px; }
  .faint-name {
    position: absolute; left: 50px; top: 390px; transform: rotate(-28deg); transform-origin: left top;
    font-weight: 700; font-size: 120px; color: var(--faint-grey); opacity: .75; white-space: nowrap; line-height: 1;
  }
  .shutoff-pad { position: absolute; left: 0; top: 338px; width: 295px; height: 148px; background: var(--alert-red); }
  .shutoff-label {
    position: absolute; left: 298px; top: 340px; width: 100px; height: 146px;
    display: flex; align-items: center; justify-content: center;
  }
  .shutoff-label p {
    transform: rotate(90deg); white-space: nowrap; font-weight: 700; font-size: 27px;
    line-height: .95; text-align: left;
  }
  .shutoff-label .red { color: var(--alert-red); display: block; }
  .shutoff-label .yellow { color: var(--hazard-yellow); display: block; }

  /* Caution label */
  .caution-panel { left: 445px; top: 368px; width: 193px; height: 162px; }
  .caution-text {
    position: absolute; left: 12px; right: 12px; top: 52px; height: 54px;
    border-top: 5px solid var(--hazard-yellow); border-bottom: 5px solid var(--hazard-yellow);
    color: var(--hazard-yellow); font-weight: 700; font-size: 40px; line-height: 44px; text-align: center;
  }

  /* Control panel */
  .control-panel { left: 445px; top: 540px; width: 400px; height: 205px; }
  .switch-pad { position: absolute; left: 191px; top: 0; width: 145px; height: 110px; background: var(--hazard-yellow); }
  .control-label { position: absolute; font-weight: 700; font-size: 16px; letter-spacing: .3px; }
  .control-label.on-dark { color: var(--hazard-yellow); }
  .control-label.on-yellow { color: var(--hazard-black); }

  /* Long side banner */
  .banner-panel { left: 30px; top: 760px; width: 970px; height: 218px; }
  .banner-name {
    position: absolute; right: 40px; top: 62px; text-align: left;
    font-weight: 700; color: var(--chalk); line-height: 1;
  }
  .banner-name .line-1 { display: block; font-size: 56px; }
  .banner-name .line-2 { display: block; font-size: 38px; margin-left: 120px; }
  .origin-badge {
    position: absolute; left: 55px; top: 150px; width: 215px; height: 50px;
    border: 5px solid var(--alert-red); border-radius: 8px;
  }
</style>
</head>
<body>
<main class="sheet">

  <header class="title-block">
    <h1 class="brand-name"><span class="line-1">TusklineDrill</span><span class="line-2">Cutter</span></h1>
    <p class="title-caption">Vinyl Wrap Designs</p>
  </header>

  <!-- End panel with eco mark placeholder -->
  <section class="panel end-panel">
    <div class="texture" role="img" aria-label="Dark stone texture with halftone dots"></div>
    <svg class="overlay" viewBox="0 0 400 200">
      <polygon points="230,0 245,0 350,200 335,200" fill="var(--accent-blue)"/>
      <polygon points="255,0 262,0 367,200 360,200" fill="var(--accent-blue)"/>
      <g fill="var(--faint-grey)" opacity=".7">
        <polygon points="220,160 232,160 222,175 210,175"/><polygon points="245,160 257,160 247,175 235,175"/>
        <polygon points="270,160 282,160 272,175 260,175"/><polygon points="295,160 307,160 297,175 285,175"/>
        <polygon points="320,160 332,160 322,175 310,175"/><polygon points="345,160 357,160 347,175 335,175"/>
        <polygon points="370,160 382,160 372,175 360,175"/><polygon points="395,160 407,160 397,175 385,175"/>
      </g>
      <circle cx="68" cy="100" r="42" fill="none" stroke="var(--muted-grey)" stroke-width="6" opacity=".85"/>
    </svg>
  </section>

  <!-- Top and side panel -->
  <section class="panel side-panel">
    <div class="texture" role="img" aria-label="Dark stone texture with slate blue blocks"></div>
    <div class="faint-name">TusklineDrill</div>
    <svg class="overlay" viewBox="0 0 400 513">
      <polygon points="30,250 38,250 10,300 2,300" fill="var(--faint-grey)"/>
      <polygon points="125,290 133,290 105,340 97,340" fill="var(--accent-blue)"/>
      <!-- hazard bands -->
      <rect x="0" y="310" width="400" height="28" fill="var(--hazard-black)"/>
      <g fill="var(--hazard-yellow)">
        <polygon points="0,310 14,310 0,332"/>
        <polygon points="30,310 48,310 30,338 12,338"/><polygon points="66,310 84,310 66,338 48,338"/>
        <polygon points="102,310 120,310 102,338 84,338"/><polygon points="138,310 156,310 138,338 120,338"/>
        <polygon points="174,310 192,310 174,338 156,338"/><polygon points="210,310 228,310 210,338 192,338"/>
        <polygon points="246,310 264,310 246,338 228,338"/><polygon points="282,310 300,310 282,338 264,338"/>
        <polygon points="318,310 336,310 318,338 300,338"/><polygon points="354,310 372,310 354,338 336,338"/>
        <polygon points="390,310 408,310 390,338 372,338"/>
      </g>
      <rect x="0" y="486" width="400" height="27" fill="var(--hazard-black)"/>
      <g fill="var(--hazard-yellow)">
        <polygon points="30,486 48,486 30,513 12,513"/><polygon points="66,486 84,486 66,513 48,513"/>
        <polygon points="102,486 120,486 102,513 84,513"/><polygon points="138,486 156,486 138,513 120,513"/>
        <polygon points="174,486 192,486 174,513 156,513"/><polygon points="210,486 228,486 210,513 192,513"/>
        <polygon points="246,486 264,486 246,513 228,513"/><polygon points="282,486 300,486 282,513 264,513"/>
        <polygon points="318,486 336,486 318,513 300,513"/><polygon points="354,486 372,486 354,513 336,513"/>
        <polygon points="390,486 408,486 390,513 372,513"/>
      </g>
    </svg>
    <div class="shutoff-pad"></div>
    <div class="shutoff-label">
      <p><span class="red">EMERGENCY</span><span class="yellow">SHUT-OFF</span><span class="red">SWITCH</span></p>
    </div>
  </section>

  <!-- Caution label -->
  <section class="panel caution-panel">
    <div class="texture" role="img" aria-label="Dark stone texture"></div>
    <svg class="overlay" viewBox="0 0 193 162">
      <rect x="0" y="0" width="193" height="24" fill="var(--hazard-black)"/>
      <g fill="var(--hazard-yellow)">
        <polygon points="10,0 26,0 10,24 -6,24"/><polygon points="42,0 58,0 42,24 26,24"/>
        <polygon points="74,0 90,0 74,24 58,24"/><polygon points="106,0 122,0 106,24 90,24"/>
        <polygon points="138,0 154,0 138,24 122,24"/><polygon points="170,0 186,0 170,24 154,24"/>
        <polygon points="202,0 218,0 202,24 186,24"/>
      </g>
      <rect x="0" y="137" width="193" height="25" fill="var(--hazard-black)"/>
      <g fill="var(--hazard-yellow)">
        <polygon points="10,137 26,137 10,162 -6,162"/><polygon points="42,137 58,137 42,162 26,162"/>
        <polygon points="74,137 90,137 74,162 58,162"/><polygon points="106,137 122,137 106,162 90,162"/>
        <polygon points="138,137 154,137 138,162 122,162"/><polygon points="170,137 186,137 170,162 154,162"/>
        <polygon points="202,137 218,137 202,162 186,162"/>
      </g>
    </svg>
    <div class="caution-text">CAUTION!</div>
  </section>

  <!-- Controls panel -->
  <section class="panel control-panel">
    <div class="texture" role="img" aria-label="Dark stone texture with halftone dots"></div>
    <svg class="overlay" viewBox="0 0 400 205">
      <polygon points="235,110 243,110 300,205 292,205" fill="var(--faint-grey)" opacity=".6"/>
      <polygon points="300,40 308,40 380,205 372,205" fill="var(--accent-blue)"/>
      <g fill="var(--faint-grey)" opacity=".6">
        <polygon points="40,18 52,18 42,34 30,34"/><polygon points="64,18 76,18 66,34 54,34"/>
        <polygon points="88,18 100,18 90,34 78,34"/><polygon points="112,18 124,18 114,34 102,34"/>
        <polygon points="340,18 352,18 342,34 330,34"/><polygon points="364,18 376,18 366,34 354,34"/>
      </g>
      <rect x="0" y="0" width="16" height="205" fill="var(--hazard-black)"/>
      <g fill="var(--hazard-yellow)">
        <polygon points="0,8 16,-8 16,6 0,22"/><polygon points="0,36 16,20 16,34 0,50"/>
        <polygon points="0,64 16,48 16,62 0,78"/><polygon points="0,92 16,76 16,90 0,106"/>
        <polygon points="0,120 16,104 16,118 0,134"/><polygon points="0,148 16,132 16,146 0,162"/>
        <polygon points="0,176 16,160 16,174 0,190"/><polygon points="0,204 16,188 16,202 0,218"/>
      </g>
    </svg>
    <div class="switch-pad"></div>
    <span class="control-label on-yellow" style="left:214px; top:8px;">OFF</span>
    <span class="control-label on-yellow" style="left:292px; top:8px;">ON</span>
    <span class="control-label on-dark" style="left:30px; top:173px;">SPEED CONTROLER</span>
    <span class="control-label on-dark" style="left:276px; top:173px;">RESET</span>
  </section>

  <!-- Long side banner -->
  <section class="panel banner-panel">
    <div class="texture" role="img" aria-label="Dark stone texture with slate blue blocks and halftone dots"></div>
    <svg class="overlay" viewBox="0 0 970 218">
      <polygon points="0,155 150,32 160,40 0,172" fill="var(--accent-blue)"/>
      <polygon points="0,188 90,66 100,72 0,205" fill="var(--chalk)"/>
      <polygon points="545,0 562,0 695,218 678,218" fill="var(--chalk)"/>
      <polygon points="640,150 652,150 690,218 678,218" fill="var(--accent-blue)"/>
      <polygon points="665,150 677,150 715,218 703,218" fill="var(--accent-blue)"/>
      <g fill="var(--faint-grey)" opacity=".7">
        <polygon points="10,50 24,50 14,66 0,66"/><polygon points="38,50 52,50 42,66 28,66"/>
        <polygon points="66,50 80,50 70,66 56,66"/><polygon points="94,50 108,50 98,66 84,66"/>
        <polygon points="122,50 136,50 126,66 112,66"/><polygon points="150,50 164,50 154,66 140,66"/>
        <polygon points="178,50 192,50 182,66 168,66"/><polygon points="206,50 220,50 210,66 196,66"/>
        <polygon points="234,50 248,50 238,66 224,66"/><polygon points="262,50 276,50 266,66 252,66"/>
      </g>
    </svg>
    <div class="origin-badge"></div>
    <div class="banner-name"><span class="line-1">TusklineDrill</span><span class="line-2">Cutter</span></div>
  </section>

</main>
</body>
</html>
```